8.5 x 11 flyer for Hormone Replacement Services for Women

You created a flyer for us that targets men. This flyer will be similar but it is targeted for women.

Here is website with the info. https://www.willowcarehealth.com/services/hormone-replacement

The flyer you created - https://www.artbidhub.com/design/58314092

```html
<!DOCTYPE html>
<html lang="en">
<head>
<meta charset="utf-8">
<title>Willow Care Group – Hormone Replacement Flyer</title>
<link rel="stylesheet" href="https://fonts.googleapis.com/css2?family=Jost:wght@300;400;500;600;700&display=swap">
<style>
  :root{
    --orange:#f7a440;
    --ink:#1a1a1a;
    --text:#4a4a4a;
    --sky:#e4f3fb;
    --sky-soft:#eaf5fc;
    --grey:#666a6d;
    --white:#ffffff;
    --stage:#2a2a2a;
  }
  *{box-sizing:border-box;margin:0;padding:0}
  html,body{width:1200px;height:900px;overflow:hidden}
  body{background:var(--stage);font-family:'Jost',sans-serif;position:relative;color:var(--ink)}
  .flyer{position:absolute;top:150px;width:461px;height:599px;overflow:hidden;background:var(--sky)}
  .flyer--front{left:105px}
  .flyer--back{left:650px;background:var(--sky-soft)}
  .abs{position:absolute}
  .shapes{position:absolute;left:0;top:0}

  /* front */
  .hero-photo{position:absolute;left:0;top:0;width:461px;height:300px;
    background:linear-gradient(90deg,#ffffff 0%,#f3f1ea 22%,#d9cdb8 45%,#c89a80 60%,#9fb6c8 72%,#7d9e5a 88%,#5f8a3c 100%)}
  .brand{display:flex;align-items:center;gap:6px;font-weight:600;color:var(--ink);line-height:1}
  .brand__dot{width:22px;height:22px;border-radius:50%;background:var(--orange);flex:none}
  .front-brand{left:20px;top:62px;font-size:38px}
  .headline{left:23px;top:124px;line-height:1.08;font-size:22px;font-weight:400;color:var(--ink)}
  .headline strong{display:block;font-size:27px;font-weight:600}
  .group-name{left:66px;top:284px;font-size:18px;font-weight:500;color:var(--orange)}
  .group-sub{left:66px;top:312px;font-size:10.4px;letter-spacing:.2px}
  .intro{left:66px;top:331px;width:390px;font-size:6.6px;line-height:9.8px;color:var(--text)}
  .slogan{right:17px;text-align:right}
  .slogan--feel{top:392px;font-size:26px;font-weight:700;letter-spacing:.3px}
  .slogan--live{top:428px;font-size:20px;font-weight:300}
  .accent{color:var(--orange)}
  .web{right:23px;top:466px;font-size:8.7px;color:var(--orange);display:flex;align-items:center;gap:8px}
  .price{left:49px;top:414px;width:100px;height:100px;border-radius:50%;
    background:radial-gradient(circle at 40% 35%,#7a7e81,var(--grey));color:var(--white);text-align:center;padding-top:26px}
  .price__amount{font-size:29px;font-weight:700;line-height:1}
  .price__term{font-size:12.5px;font-weight:500;margin-top:4px}

  /* footer */
  .office{top:528px;color:var(--white)}
  .office--yuma{left:36px}
  .office--tucson{left:250px}
  .office h3{font-size:11.4px;font-weight:400;margin-bottom:5px;white-space:nowrap}
  .office li{list-style:none;font-size:6.8px;font-weight:300;display:flex;align-items:center;gap:6px;height:15px;white-space:nowrap}
  .office svg{flex:none}
  .divider{left:230px;top:529px;width:1px;height:60px;background:var(--white)}

  /* back */
  .qa-title{left:37px;top:28px;font-size:23px;font-weight:400;letter-spacing:2.4px;white-space:nowrap}
  .qa-title b{color:var(--orange);font-weight:600;letter-spacing:3px}
  .col{position:absolute;width:192px}
  .col h4{font-size:8px;font-weight:400;line-height:9px;margin-bottom:6px}
  .col h4 span{color:var(--orange)}
  .col p{font-size:5.6px;line-height:7.6px;color:var(--text);margin-bottom:5px}
  .bullets{list-style:none;margin:6px 0 8px}
  .bullets li{font-size:5.6px;color:var(--text);height:10.3px;display:flex;align-items:center;gap:5px}
  .bullets li::before{content:"";width:4px;height:4px;border-radius:50%;background:var(--orange);flex:none}
  .services-title{font-size:10.6px;color:var(--orange);font-weight:400;margin:8px 0 3px}
  .back-brand{left:283px;top:448px;font-size:38px}
</style>
</head>
<body>

<!-- Front -->
<section class="flyer flyer--front">
  <div class="hero-photo" role="img" aria-label="Photo of a smiling woman in a light blue cardigan outdoors in a sunny garden"></div>

  <svg class="shapes" width="461" height="599" viewBox="0 0 461 599" aria-hidden="true">
    <path d="M0,262 Q220,214 461,282 L461,599 L0,599 Z" fill="#ffffff"/>
    <path d="M0,268 Q220,222 461,290 L461,316 Q220,236 0,278 Z" fill="#f7a440"/>
    <path d="M0,280 Q220,244 461,318 L461,599 L0,599 Z" fill="#e4f3fb"/>
    <path d="M0,423 Q190,506 461,498 L461,506 Q190,518 0,448 Z" fill="#1a1a1a"/>
    <path d="M0,458 Q190,522 461,510 L461,599 L0,599 Z" fill="#f7a440"/>
  </svg>

  <div class="abs brand front-brand"><span class="brand__dot"></span>Willow</div>
  <h1 class="abs headline">Hormone<strong>Replacement</strong>Specialist</h1>

  <h2 class="abs group-name">Willow Care Group</h2>
  <p class="abs group-sub">Health and Wellness Center located in Yuma, AZ &amp; Tucson, AZ</p>
  <p class="abs intro">Are you looking for a way to counter the signs and symptoms of aging? About 1.4 million women rely on bioidentical hormone replacement, according to the Continental Menopause Council. Willow Care Group offers this anti-aging therapy to naturally restore the estrogen and progesterone your body has lost. See if you’re a candidate for hormone replacement by calling the Tucson or Yuma, Arizona, office or booking a consultation online.</p>

  <p class="abs slogan slogan--feel">FEEL <span class="accent">AMAZIBG.</span></p>
  <p class="abs slogan slogan--live">LIVE <span class="accent">BETTER.</span></p>
  <p class="abs web">
    <svg width="10" height="10" viewBox="0 0 10 10"><circle cx="5" cy="5" r="4.5" fill="#f7a440"/><path d="M2,3 Q4,4 3,6 M6,2 Q7,5 8,6" stroke="#fff" stroke-width="1" fill="none"/></svg>
    www.willowcarehealth.com
  </p>

  <div class="abs price">
    <div class="price__amount">$150</div>
    <div class="price__term">Per Month</div>
  </div>

  <div class="abs divider"></div>
  <div class="abs office office--yuma">
    <h3>Willow Care Group, Yuma, AZ</h3>
    <ul>
      <li><svg width="8" height="8" viewBox="0 0 8 8"><circle cx="4" cy="4" r="3.4" stroke="#fff" stroke-width=".8" fill="none"/><path d="M2.7,2.3 L3.5,3.3 L3.1,3.8 Q3.6,4.6 4.4,5 L4.8,4.6 L5.8,5.3 L5.3,6 Q3,5.6 2.2,3 Z" fill="#fff"/></svg>(appointments) : 928-555-0142</li>
      <li><svg width="8" height="8" viewBox="0 0 8 8"><path d="M1,1 L2.6,1 L3.2,2.8 L2.3,3.5 Q3.3,5 4.6,5.8 L5.3,4.9 L7,5.6 L7,7 Q2.2,7 1,1 Z" fill="#fff"/></svg>(general inquiries) : 928-555-0142</li>
      <li><svg width="8" height="9" viewBox="0 0 8 9"><path d="M4,9 Q0.5,5 0.5,3.5 A3.5,3.5 0 0 1 7.5,3.5 Q7.5,5 4,9 Z" fill="#fff"/><circle cx="4" cy="3.5" r="1.3" fill="#f7a440"/></svg>1460 South 9th Avenue , Suite B, Yuma, AZ 85364</li>
    </ul>
  </div>
  <div class="abs office office--tucson">
    <h3>Willow Care Group, Tucson, AZ</h3>
    <ul>
      <li><svg width="8" height="8" viewBox="0 0 8 8"><circle cx="4" cy="4" r="3.4" stroke="#fff" stroke-width=".8" fill="none"/><path d="M2.7,2.3 L3.5,3.3 L3.1,3.8 Q3.6,4.6 4.4,5 L4.8,4.6 L5.8,5.3 L5.3,6 Q3,5.6 2.2,3 Z" fill="#fff"/></svg>(appointments): 520-555-0187</li>
      <li><svg width="8" height="8" viewBox="0 0 8 8"><path d="M1,1 L2.6,1 L3.2,2.8 L2.3,3.5 Q3.3,5 4.6,5.8 L5.3,4.9 L7,5.6 L7,7 Q2.2,7 1,1 Z" fill="#fff"/></svg>(general inquiries) : 520-555-0187</li>
      <li><svg width="8" height="9" viewBox="0 0 8 9"><path d="M4,9 Q0.5,5 0.5,3.5 A3.5,3.5 0 0 1 7.5,3.5 Q7.5,5 4,9 Z" fill="#fff"/><circle cx="4" cy="3.5" r="1.3" fill="#f7a440"/></svg>318 East Verde Road, Suite 210, Tucson, AZ 85711</li>
    </ul>
  </div>
</section>

<!-- Back -->
<section class="flyer flyer--back">
  <svg class="shapes" width="461" height="599" viewBox="0 0 461 599" aria-hidden="true">
    <path d="M0,423 Q190,506 461,498 L461,506 Q190,518 0,448 Z" fill="#1a1a1a"/>
    <path d="M0,458 Q190,522 461,510 L461,599 L0,599 Z" fill="#f7a440"/>
  </svg>

  <h2 class="abs qa-title">Hormone Replacement <b>Q &amp; A</b></h2>

  <div class="col" style="left:36px;top:62px">
    <h4>What is hormone <span>replacement for women?</span></h4>
    <p>Although there’s no escaping the march of time, modern medicine can now slow the tell-tale signs of aging through bioidentical hormone replacement. The cutting-edge therapy can be a safe, effective solution to combat the effects of aging with natural hormones that mimic the ones in your own body.</p>
    <p>The treatment helps to restore and balance your hormone levels, with precise doses of progesterone, estrogen, DHEA, and more. The goal is to improve your quality of life by returning your hormone levels to normal.</p>
    <p>Your provider at Willow Care Group recommends hormone replacement to relieve perimenopausal and menopausal symptoms. Menopause occurs at age 52 for the average woman. Through this process, your ovaries make less and less estrogen, causing several uncomfortable symptoms.</p>
    <p>Bioidentical hormones help replace the hormones your body has lost. Bioidentical hormones are produced from plants and contain all of the same properties as the estrogen your body makes. Beyond replacing estrogen, these natural hormones supplement progesterone and other hormones your body has lost.</p>
  </div>

  <div class="col" style="left:36px;top:248px">
    <h4>Are bioidentical hormones better than<br><span>synthetics?</span></h4>
    <p>Hormones used in traditional replacement therapy are usually made of synthetic materials or animal urine. In comparison, bioidentical hormones are created from plant materials, a more natural alternative.</p>
    <p>The providers at Willow Care Group recommend natural estrogen instead of synthetic estrogen because of its benefits.</p>
    <h4 class="services-title">Our Services</h4>
    <ul class="bullets">
      <li>Hormone Replacement</li>
      <li>Testosterone Replacement Therapy</li>
      <li>ED</li>
      <li>Toenail Fungus</li>
      <li>Scar Removal</li>
      <li>Dark Sports</li>
      <li>Laser Hair Removal</li>
      <li>Acne</li>
    </ul>
  </div>

  <div class="col" style="left:248px;top:62px;width:202px">
    <h4>What are the benefits of estrogen <span>hormone therapy?</span></h4>
    <p>Hormone therapy to replace the estrogen you’ve lost helps to protect you from the following ailments and symptoms:</p>
    <ul class="bullets">
      <li>Heart disease</li>
      <li>Stroke</li>
      <li>Osteoporosis</li>
      <li>Alzheimer’s disease and memory disorders</li>
      <li>Urinary incontinence</li>
      <li>Hot flashes</li>
      <li>Mood swings</li>
      <li>Fatigue</li>
    </ul>
    <p>The therapy also helps with vaginal atrophy to restore your intimate wellbeing.</p>
    <p>Your provider at Willow Care Group also recommends balancing estrogen with progesterone to achieve all the benefits of hormone replacement.</p>
  </div>

  <div class="col" style="left:248px;top:248px;width:202px">
    <h4>What are the benefits of estrogen <span>hormone therapy?</span></h4>
    <p>Progesterone, a hormone secreted by your ovaries until menopause, helps to protect against a number of health conditions, including:</p>
    <ul class="bullets">
      <li>Breast and uterine cancer</li>
      <li>Ovarian cysts</li>
      <li>Fibrocystic disease</li>
      <li>Bone loss</li>
    </ul>
    <p>Progesterone also causes common menopausal symptoms, which is why your provider recommends a balanced regime that includes both estrogen and progesterone.</p>
    <p>If you’re experiencing changes in your body because of aging, find out if natural bioidentical hormone therapy is right for you. Call Willow Care Group today, or book a consultation online.</p>
  </div>

  <div class="abs brand back-brand"><span class="brand__dot"></span>Willow</div>

  <div class="abs divider"></div>
  <div class="abs office office--yuma">
    <h3>Willow Care Group, Yuma, AZ</h3>
    <ul>
      <li><svg width="8" height="8" viewBox="0 0 8 8"><circle cx="4" cy="4" r="3.4" stroke="#fff" stroke-width=".8" fill="none"/><path d="M2.7,2.3 L3.5,3.3 L3.1,3.8 Q3.6,4.6 4.4,5 L4.8,4.6 L5.8,5.3 L5.3,6 Q3,5.6 2.2,3 Z" fill="#fff"/></svg>(appointments) : 928-555-0142</li>
      <li><svg width="8" height="8" viewBox="0 0 8 8"><path d="M1,1 L2.6,1 L3.2,2.8 L2.3,3.5 Q3.3,5 4.6,5.8 L5.3,4.9 L7,5.6 L7,7 Q2.2,7 1,1 Z" fill="#fff"/></svg>(general inquiries) : 928-555-0142</li>
      <li><svg width="8" height="9" viewBox="0 0 8 9"><path d="M4,9 Q0.5,5 0.5,3.5 A3.5,3.5 0 0 1 7.5,3.5 Q7.5,5 4,9 Z" fill="#fff"/><circle cx="4" cy="3.5" r="1.3" fill="#f7a440"/></svg>1460 South 9th Avenue , Suite B, Yuma, AZ 85364</li>
    </ul>
  </div>
  <div class="abs office office--tucson">
    <h3>Willow Care Group, Tucson, AZ</h3>
    <ul>
      <li><svg width="8" height="8" viewBox="0 0 8 8"><circle cx="4" cy="4" r="3.4" stroke="#fff" stroke-width=".8" fill="none"/><path d="M2.7,2.3 L3.5,3.3 L3.1,3.8 Q3.6,4.6 4.4,5 L4.8,4.6 L5.8,5.3 L5.3,6 Q3,5.6 2.2,3 Z" fill="#fff"/></svg>(appointments): 520-555-0187</li>
      <li><svg width="8" height="8" viewBox="0 0 8 8"><path d="M1,1 L2.6,1 L3.2,2.8 L2.3,3.5 Q3.3,5 4.6,5.8 L5.3,4.9 L7,5.6 L7,7 Q2.2,7 1,1 Z" fill="#fff"/></svg>(general inquiries) : 520-555-0187</li>
      <li><svg width="8" height="9" viewBox="0 0 8 9"><path d="M4,9 Q0.5,5 0.5,3.5 A3.5,3.5 0 0 1 7.5,3.5 Q7.5,5 4,9 Z" fill="#fff"/><circle cx="4" cy="3.5" r="1.3" fill="#f7a440"/></svg>318 East Verde Road, Suite 210, Tucson, AZ 85711</li>
    </ul>
  </div>
</section>

</body>
</html>
```